依頼概要
■ 依頼の目的/概要

スキンケア商品のパッケージデザイン(容器と外装箱)を依頼させて頂きます。

■ パッケージデザインへの要望

清潔感が感じられ、スタイリッシュで洒落たデザインを希望します。
ターゲットは30代以上の女性です。年配の方にも受け入れられるデザインでお願いします。

■ 商品情報

ブランド名「BELUMIS」ベルミスは関西弁「洗(あろ)てな」から付けました。真っ黒の石鹸です。
現在黒いケースに入れているのですが「男っぽい」のでリニューアルする事にしました。
清潔感のある白を基調にした箱から真っ黒の石鹸がでてくるイメージです。
同時に、ローション、ピーリングジェル、モイストジェルも開発し、BELUMISブランドで販売します。
社名のフェノワにちなんで今回このシリーズにサクラエキスを入れた事もありサクラの花びらを1ポイントに入れたいです。
これらの商品を入れる配送用のケース、トライアルキットのケースもオーダーすることになります。

まとめます。
①石鹸の箱のデザイン
②ローション、ピーリングジェルのボトルデザイン。ボトルは乳白色です。
③モイストジェルのジャーデザイン。ジャーは乳白色です。
上記3点を共通のイメージで仕上げていただきたいですが今回のコンペでは

②のみを募集させて頂きます。
~~~~~~~~~~~~~~~~~~~~~~~~~~~~~
配送用、トライアルキットのケースについては①〜③が決まってから依頼した方がいいのかも知れませんが、
トータルで考えていただくのもいいのかと思い、あえて記載させていただきました。

■ パッケージの情報

ローション、ピーリングジェルはpdfファイルを添付しました。

■ 納品ファイルの希望

イラストレーター形式もしくはフォトショップ形式

■ 進め方

弊社の希望するイメージに近い提案を1つ(場合によって複数)選択させて頂きます。希望に近づけるために、修正要望を個別にさせて頂くこともあります。コンペ方式のため、修正後に当選されない場合も、どうかご了承ください。

■ その他/注意点

選択させて頂いたデザインの著作権(財産権)等の扱いはTaskora利用規約に従い、弊社に譲渡をお願いします。フォントや画像素材などを利用する場合は上記利用用途に使用できることを確認し、第三者の知的財産権等に注意して下さい。
商品コンセプトは当社のHPをご覧になってください。
http://www.belumis-example.com/
ちなみにこのHPも新商品投入にともないスキンケア全般を扱うHPとしてリニューアルします。

belumisのロゴ(ai)、fenowaのロゴ(jpg)しました。
fenwoaのaiデータはあとでアップします。
ファイルが添付されていなかったようです。
ジャーのpdf資料上げます。
「和」のイメージの提案は基本的に考えていません。

容器にローションの中身を入れると桜色になります。
ピーリングジェルはグレー、モイストジェルはうぐいす色になります。

箱に入ったイメージ、アップします。
トライアルキットもアップします。
依頼内容を縮小させていただきました関係から提案の締め切り期限を延長させていただきます。お盆もありますので21日まで締め切りを延ばさせていただきます。
何点か提案していただきこちらの思いも
①Belumisのロゴ(添付のaiデータ)をヨコに寝かした(キャップを左にしてBelumisになるように)デザインもいいのでは?
②fenowaのロゴは成分表示などを記載する裏面に使用する。
③表面にはサクラの花びら(ピンク)をどこかに入れたい。
④色数は2〜3色
⑤ボトルの色が乳白色ですが中身の入りは見えます。Pジェルはチャコールグレー、ローションはチェリーピンクです。どちらの色にも映えるようにお願いします。

以上です。
■ 選んだ理由

シンプルである事。
サクラエキスをイメージできるモチーフ。
belumisのコンセプトをうまく表現しているところ。

■ 提案者全員へのお礼・コメント

タスコラの皆様たくさんの提案していただき心からお礼申し上げます。
すごく勉強になりました。

今後また機会がありましたら依頼したいと思います。

```html
<!DOCTYPE html>
<html lang="ja">
<head>
<meta charset="utf-8">
<title>Belumis ボトルデザイン</title>
<link rel="stylesheet" href="https://fonts.googleapis.com/css2?family=Josefin+Sans:wght@300&family=Noto+Sans+JP:wght@400&display=swap">
<style>
  :root {
    --page: #ffffff;
    --outline: #c9c6bb;
    --cream: #f7f5ea;
    --cream-deep: #ece8d6;
    --cap: #fbfaf4;
    --pink-light: #f9dde4;
    --pink: #f3c3cf;
    --badge: #4b4a48;
    --badge-text: #ffffff;
    --petal: #ea8fab;
  }
  html, body {
    margin: 0;
    padding: 0;
    background: var(--page);
    overflow: hidden;
  }
  .canvas {
    width: 813px;
    height: 1200px;
    display: block;
  }
  .part { stroke: var(--outline); stroke-width: 2; }
  .cream { fill: var(--cap); }
  .gel-body { fill: url(#gelFill); }
  .lotion-body { fill: url(#lotionFill); }
  .badge { fill: var(--badge); }
  .brand-name {
    fill: var(--badge-text);
    font-family: "Josefin Sans", sans-serif;
    font-weight: 300;
    font-size: 44px;
  }
  .product-label {
    fill: var(--badge-text);
    font-family: "Noto Sans JP", sans-serif;
    font-size: 17px;
  }
  .petals { fill: var(--petal); }
  .nozzle { fill: none; stroke: var(--outline); stroke-width: 14; stroke-linecap: round; }
  .nozzle-inner { fill: none; stroke: var(--cap); stroke-width: 10; stroke-linecap: round; }
  .liquid-line { fill: none; stroke: var(--outline); stroke-width: 1.5; opacity: .6; }
</style>
</head>
<body>
<svg class="canvas" viewBox="0 0 813 1200" xmlns="http://www.w3.org/2000/svg">
  <defs>
    <linearGradient id="gelFill" x1="0" y1="0" x2="1" y2="0">
      <stop offset="0" stop-color="var(--cream-deep)"/>
      <stop offset=".5" stop-color="var(--cream)"/>
      <stop offset="1" stop-color="var(--cream-deep)"/>
    </linearGradient>
    <linearGradient id="lotionFill" x1="0" y1="0" x2="1" y2="0">
      <stop offset="0" stop-color="var(--pink)"/>
      <stop offset=".5" stop-color="var(--pink-light)"/>
      <stop offset="1" stop-color="var(--pink)"/>
    </linearGradient>
  </defs>

  <!-- Peeling gel pump bottle -->
  <g class="bottle bottle--peeling-gel">
    <path class="nozzle" d="M262 62 H150 Q118 62 114 100 V112"/>
    <path class="nozzle-inner" d="M262 62 H150 Q118 62 114 100 V112"/>
    <rect class="part cream" x="255" y="38" width="72" height="72" rx="6"/>
    <rect class="part cream" x="278" y="110" width="28" height="42"/>
    <rect class="part cream" x="215" y="150" width="155" height="122" rx="6"/>
    <rect class="part cream" x="200" y="270" width="185" height="16" rx="3"/>
    <rect class="part gel-body" x="95" y="284" width="315" height="866" rx="14"/>
    <path class="liquid-line" d="M97 335 Q180 318 252 335 T408 330"/>
    <rect class="badge" x="155" y="505" width="185" height="175"/>
    <text class="brand-name" x="247" y="606" text-anchor="middle">Belumis</text>
    <path class="petals" role="img" aria-label="桜の花びら" d="M205 700 h55 a18 18 0 0 1 18 18 v55 a18 18 0 0 1 -18 18 h-55 a18 18 0 0 1 -18 -18 v-55 a18 18 0 0 1 18 -18 z"/>
    <rect class="badge" x="155" y="1088" width="200" height="30"/>
    <text class="product-label" x="165" y="1109">ピーリングジェル</text>
  </g>

  <!-- Lotion bottle -->
  <g class="bottle bottle--lotion">
    <rect class="part cream" x="477" y="80" width="241" height="118" rx="10"/>
    <rect class="part lotion-body" x="477" y="196" width="241" height="954" rx="12"/>
    <path class="liquid-line" d="M479 236 Q560 222 620 236 T716 232"/>
    <rect class="badge" x="520" y="430" width="172" height="175"/>
    <text class="brand-name" x="606" y="531" text-anchor="middle">Belumis</text>
    <path class="petals" role="img" aria-label="桜の花びら" d="M625 620 h50 a18 18 0 0 1 18 18 v50 a18 18 0 0 1 -18 18 h-50 a18 18 0 0 1 -18 -18 v-50 a18 18 0 0 1 18 -18 z"/>
    <rect class="badge" x="540" y="1088" width="140" height="30"/>
    <text class="product-label" x="550" y="1109">ローション</text>
  </g>
</svg>
</body>
</html>
```